Business Card Design Project for Architecture and Interior Design company

We need a business card design and logo for an architecture and design firm located in Santiago de Chile. It´s a small company, and the name is "Ostrevo" ("Ostr" from my surname Ostrini, and "arq" for arquitectura or architecture. But it would also be nice that the logo comunicates de Word game "Bella" as beautiful in italian, and "arq" as architecture".
The idea is to give a delicate, elegant and sofisticated, yet fresh image. Would prefer grey black and white colors, but wouldn´t mind to use another additional color.
I allready have a web page www.ostrevo-studio.example, but would like to improve the logo design.
Please contact if any further information is requiered.
Reason: Need a more arquitectural and desing spirit in the cards. Few of them give that idea.

```html
<!DOCTYPE html>
<html lang="es">
<head>
<meta charset="utf-8">
<title>Ostrevo – tarjeta de presentación</title>
<link href="https://fonts.googleapis.com/css2?family=Comfortaa:wght@400;700&display=swap" rel="stylesheet">
<style>
  :root {
    --ink: #231f20;
    --red: #e8212c;
    --paper: #ffffff;
    --stage: #d6d6d6;
    --blueprint-light: #f3f6fb;
    --blueprint-mid: #d3deec;
    --font-main: "Comfortaa", sans-serif;
  }
  * { box-sizing: border-box; margin: 0; padding: 0; }
  html, body {
    width: 1105px; height: 1200px; overflow: hidden;
    background: var(--stage);
    font-family: var(--font-main);
  }
  .canvas {
    position: relative; width: 1105px; height: 1200px;
    display: flex; flex-direction: column; align-items: center; justify-content: center; gap: 44px;
  }
  .card {
    position: relative; width: 960px; height: 548px;
    background: var(--paper); overflow: hidden;
    box-shadow: 0 2px 8px rgba(0,0,0,.18);
  }

  /* ---------- front ---------- */
  .front__illustration {
    position: absolute; left: 500px; top: 0; width: 460px; height: 548px;
    background:
      linear-gradient(150deg, rgba(255,255,255,0) 40%, rgba(232,33,44,.35) 75%, rgba(255,255,255,0) 90%),
      linear-gradient(110deg, #eeeeee 0%, #b68a5a 35%, #d8c04a 45%, #9a7a58 55%, #d9d9d9 75%, #f2f2f2 100%);
    opacity: .9;
  }
  .front__bars { position: absolute; left: 38px; top: 40px; display: flex; height: 20px; }
  .front__bars .bar--ink { width: 195px; background: var(--ink); }
  .front__bars .bar--red { width: 215px; background: var(--red); }
  .brand-name {
    position: absolute; left: 34px; top: 100px;
    font-weight: 700; font-size: 104px; line-height: 1; letter-spacing: -4px;
    color: var(--ink);
  }
  .tagline {
    position: absolute; left: 38px; top: 218px;
    font-size: 22px; color: var(--ink);
  }
  .contact { position: absolute; left: 38px; top: 316px; display: flex; flex-direction: column; gap: 18px; }
  .contact__row { display: flex; gap: 8px; height: 46px; }
  .contact__label, .contact__value {
    display: flex; align-items: center; padding: 0 10px;
    color: var(--paper); font-size: 22px;
  }
  .contact__value { font-size: 19px; letter-spacing: 1.5px; }
  .is-red { background: var(--red); }
  .is-ink { background: var(--ink); }
  .front__rule { position: absolute; left: 38px; top: 514px; width: 420px; height: 10px; background: var(--ink); }

  /* ---------- back ---------- */
  .back__blueprint {
    position: absolute; inset: 0;
    background: linear-gradient(135deg, var(--blueprint-light) 0%, #e3ebf5 45%, var(--blueprint-mid) 100%);
  }
  .back__lockup {
    position: absolute; left: 20px; top: 40px; width: 1000px; height: 520px;
    transform: rotate(-21deg); transform-origin: 50% 50%;
  }
  .back__bar { position: absolute; left: 440px; top: 70px; width: 560px; height: 26px; background: var(--red); border-radius: 13px; }
  .back__name {
    position: absolute; left: 20px; top: 110px;
    font-weight: 700; font-size: 220px; line-height: 1; letter-spacing: -8px;
    color: var(--ink);
  }
  .back__tagline { position: absolute; left: 120px; top: 345px; font-size: 46px; color: var(--ink); }
  .back__rule { position: absolute; left: 60px; top: 412px; width: 460px; height: 14px; background: var(--ink); border-radius: 7px; }
</style>
</head>
<body>
<main class="canvas">
  <section class="card card--front">
    <div class="front__illustration" role="img" aria-label="Ilustración en corte de una casa con muros de madera, aislación y planos arquitectónicos"></div>
    <div class="front__bars"><span class="bar--ink"></span><span class="bar--red"></span></div>
    <h1 class="brand-name">ostrevo</h1>
    <p class="tagline">arquitectura diseño de interiores</p>
    <div class="contact">
      <div class="contact__row">
        <span class="contact__label is-red">fono:</span>
        <span class="contact__value is-ink">+56 9 5550 1234</span>
      </div>
      <div class="contact__row">
        <span class="contact__label is-ink">contacto:</span>
        <span class="contact__value is-red">info@ostrevo-studio.example</span>
      </div>
      <div class="contact__row">
        <span class="contact__label is-red">web:</span>
        <span class="contact__value is-ink">www.ostrevo-studio.example</span>
      </div>
    </div>
    <div class="front__rule"></div>
  </section>

  <section class="card card--back">
    <div class="back__blueprint" role="img" aria-label="Plano arquitectónico azul en tonos suaves de fondo"></div>
    <div class="back__lockup">
      <div class="back__bar"></div>
      <p class="back__name">ostrevo</p>
      <p class="back__tagline">arquitectura diseño de interiores</p>
      <div class="back__rule"></div>
    </div>
  </section>
</main>
</body>
</html>
```